Finiding oppertunites in Real Estate 6.15.20

size of ad 7” x 9.6”
1-I like the ad to stand out and attract people's attention.
2-you should be able to see the text of the ad clearly .. see the attachment anything in yellow is instructions.
3-the list of topics should not be the main part of the ad
4-if you decide you want a picture or vector of a person .. (you decide)
then it should be a white male about 25-30 years old wearing a solid white or blue shirt and not long hair.
5-leave 1 inch for footer
see attachment
Good luck

Target Market(s)

potential male students 25-35 years of age

Industry/Entity Type

Education

Requirements
Must have
• will stand out and people would want to see it.
should be able to read the words of ad
Nice to have
• how to make money in real estate on one line

```html
<!DOCTYPE html>
<html lang="en">
<head>
<meta charset="UTF-8">
<title>Real Estate Career Course</title>
<link href="https://fonts.googleapis.com/css2?family=Roboto:ital,wght@0,400;0,500;0,700;0,900;1,500&family=Roboto+Condensed:wght@700&display=swap" rel="stylesheet">
<style>
  :root {
    --navy: #1c3457;
    --navy-dark: #13243f;
    --orange: #e5451d;
    --orange-bright: #f26522;
    --paper: #d9dadb;
    --paper-light: #eef0f1;
    --white: #ffffff;
    --gold: #d9a935;
    --ink: #1a1a1a;
  }
  * { box-sizing: border-box; margin: 0; padding: 0; }
  html, body { width: 876px; height: 1200px; overflow: hidden; background: #ffffff; }
  .flyer {
    position: relative;
    width: 876px;
    height: 1200px;
    overflow: hidden;
    font-family: "Roboto", Arial, sans-serif;
    background: radial-gradient(ellipse at 40% 70%, var(--paper-light) 0%, var(--paper) 55%, #b9bbbd 100%);
  }
  .hero-photo {
    position: absolute;
    left: 0; top: 0;
    width: 876px; height: 690px;
    background:
      radial-gradient(ellipse at 52% 40%, #3f6fa8 0%, rgba(63,111,168,0) 45%),
      linear-gradient(180deg, #9ea4aa 0%, #c4c8cc 35%, #dfe1e3 70%, #eceeef 100%);
  }
  .logo-block {
    position: absolute;
    left: 0; top: 0;
    width: 290px; height: 120px;
  }
  .logo-block svg { position: absolute; left: 0; top: 0; }
  .logo-name {
    position: absolute;
    left: 48px; top: 26px;
    color: var(--white);
    font-weight: 900;
    font-size: 40px;
    letter-spacing: 1px;
  }
  .course-title {
    position: absolute;
    left: 72px; top: 372px;
    color: var(--orange);
    font-family: "Roboto Condensed", Arial, sans-serif;
    font-weight: 700;
    font-size: 62px;
    line-height: 1.08;
    text-shadow: 0 2px 0 rgba(255,255,255,0.35);
  }
  .divider-band { position: absolute; left: 0; top: 640px; z-index: 1; }
  .main-copy {
    position: absolute;
    left: 40px; top: 690px;
    width: 540px;
    text-align: center;
    color: var(--navy);
  }
  .headline {
    font-weight: 900;
    font-size: 41px;
    line-height: 1.12;
  }
  .headline-underline { display: block; margin: 6px auto 0; }
  .audience {
    margin-top: 14px;
    font-weight: 500;
    font-size: 29px;
    line-height: 1.12;
  }
  .tagline {
    margin-top: 24px;
    font-style: italic;
    font-weight: 500;
    font-size: 28px;
    line-height: 1.12;
  }
  .schedule {
    position: absolute;
    left: 55px; top: 995px;
    width: 510px; height: 110px;
  }
  .schedule svg { position: absolute; left: 0; top: 0; }
  .schedule-text {
    position: absolute;
    left: 0; top: 16px; width: 510px;
    text-align: center;
    color: var(--white);
    font-weight: 700;
    font-size: 31px;
    line-height: 1.15;
  }
  .topics {
    position: absolute;
    left: 672px; top: 590px;
    width: 190px;
    z-index: 2;
    color: var(--navy-dark);
  }
  .topics-heading {
    font-weight: 700;
    font-size: 17px;
    line-height: 1.1;
    letter-spacing: 0.5px;
    text-transform: uppercase;
    margin-bottom: 8px;
  }
  .topics-list { list-style: none; }
  .topics-list li {
    display: flex;
    align-items: center;
    gap: 7px;
    font-size: 15px;
    line-height: 22px;
    font-weight: 500;
    white-space: nowrap;
  }
  .topics-list li::before {
    content: "";
    width: 9px; height: 9px;
    border: 1.5px solid var(--navy-dark);
    border-radius: 50%;
    flex: none;
  }
  .remote-badge {
    position: absolute;
    left: 697px; top: 965px;
    width: 156px; height: 156px;
    border-radius: 50%;
    background: radial-gradient(circle at 40% 35%, #2b2b2b 0%, #050505 70%);
    border: 7px solid var(--gold);
    box-shadow: 0 0 0 2px #8a6a1c, 0 4px 10px rgba(0,0,0,0.4);
    display: flex; align-items: center; justify-content: center;
    text-align: center;
    color: var(--white);
    font-weight: 700;
    font-size: 27px;
    line-height: 1.15;
  }
</style>
</head>
<body>
<main class="flyer">
  <div class="hero-photo" role="img" aria-label="Businessman in a suit holding a glowing house icon over a city skyline"></div>

  <div class="logo-block">
    <svg width="290" height="120" viewBox="0 0 290 120" aria-hidden="true">
      <path d="M0 0 H290 C270 60 230 105 150 112 C90 117 40 108 0 96 Z" fill="var(--navy)"/>
    </svg>
    <span class="logo-name">LOGO</span>
  </div>

  <h1 class="course-title">Real Estate<br>Career Course</h1>

  <svg class="divider-band" width="660" height="70" viewBox="0 0 660 70" aria-hidden="true">
    <path d="M0 34 C200 12 420 8 655 16 L660 18 C420 20 200 28 0 52 Z" fill="var(--navy)"/>
  </svg>

  <section class="main-copy">
    <h2 class="headline">How to Make Money<br>In Real Estate?</h2>
    <svg class="headline-underline" width="400" height="22" viewBox="0 0 400 22" aria-hidden="true">
      <path d="M6 14 C120 4 280 2 394 8 C300 10 160 14 20 20 Z" fill="var(--orange-bright)"/>
    </svg>
    <p class="audience">For those who have started or<br>would like to go into Real Estate</p>
    <p class="tagline">An investment in knowledge opens<br>up untold opportunities</p>
  </section>

  <div class="schedule">
    <svg width="510" height="110" viewBox="0 0 510 110" aria-hidden="true">
      <path d="M14 8 L500 2 L496 30 L508 58 L492 82 L498 104 L20 108 L4 86 L16 60 L2 34 Z" fill="var(--navy-dark)"/>
    </svg>
    <p class="schedule-text">12 Session Course<br>Classes Starting June 16</p>
  </div>

  <aside class="topics">
    <h3 class="topics-heading">A Partial<br>Listing of Topics</h3>
    <ul class="topics-list">
      <li>Single-family</li>
      <li>Multifamily</li>
      <li>Management</li>
      <li>Real Estate Concepts</li>
      <li>Real Estate law</li>
      <li>Investment properties</li>
      <li>Foreclosures</li>
      <li>Rehab</li>
      <li>Foreclosures</li>
      <li>Short sales</li>
      <li>Development</li>
      <li>Rental property</li>
      <li>HUD properties</li>
      <li>Due Diligence</li>
    </ul>
  </aside>

  <div class="remote-badge">Remote<br>Sessions</div>
</main>
</body>
</html>
```